Lottery Scratchcard templates for charities

We produce scratch cards for charities to sell to their supporters to raise funds.

We need a set of templates which can be re-used for different clients by simply replacing text, logo, prizes and a potentially a picture.

One of the templates can be plain simply using block colours
One can use generic images like a treasure chests which indicate money can be won
One templates can feature space for a photograph which can be easily replaced and updated depending on the client - example, a picture of a dog for a dog charity can easily be replaced by a picture of a football team for a club.

Target Market(s)

People who support a charity and the charities themselves

Industry/Entity Type

Charity

Colors

Designer to choose colors to be used in the design.

Requirements
Must have
• Every card will need space for:
• - The charity's logo
• - our logo
• - a panel which can be scratched off (use a plain silver, but can have an image printed on top in black only)
• - information about how to win (this can be lorem ipsum text)
• - Prizes (usually 4 or 5 prize levels of £100, £50, £10, £1)
• - Price: £1 and/or Just £1 to play
• - Small print - "Please play responsibly www.KeelbrookTrust.org."
• minimum size 4pt
• Paper size: A7, print ready
• Format: Adobe InDesign, fully editable
• Vector illustrations/design elements

```html
<!DOCTYPE html>
<html lang="en">
<head>
<meta charset="utf-8">
<title>Charity Scratchcard – Photo Template</title>
<link rel="stylesheet" href="https://fonts.googleapis.com/css2?family=Montserrat:wght@400;500;700;800&family=Raleway:wght@300&display=swap">
<style>
  :root {
    --maroon: #6a1b24;
    --orange: #ee4b23;
    --orange-deep: #e63d1f;
    --gold-mid: #d9a536;
    --gold-dark: #a97a25;
    --white: #ffffff;
    --ink: #1d1d1b;
  }
  * { box-sizing: border-box; margin: 0; padding: 0; }
  html, body { width: 1200px; height: 889px; overflow: hidden; background: #ffffff; }
  body { font-family: "Montserrat", Arial, sans-serif; color: var(--maroon); }

  .card {
    position: relative;
    width: 1200px; height: 889px;
    overflow: hidden;
    background:
      radial-gradient(circle at 440px 380px, rgba(255,255,255,0.95) 0%, rgba(255,255,255,0.6) 18%, rgba(255,255,255,0) 42%),
      conic-gradient(from 0deg at 440px 380px,
        #b9c8ec 0deg, #e4efd2 30deg, #dfe866 55deg, #f3dc5a 80deg,
        #f7b23e 105deg, #f38a2c 135deg, #ef6526 170deg, #ec5129 200deg,
        #e9463a 230deg, #e6477a 262deg, #d2559f 290deg, #a472c4 320deg, #b9c8ec 360deg);
  }

  .frame { position: absolute; inset: 0; width: 1200px; height: 889px; }

  .charity-logo {
    position: absolute; left: 40px; top: 34px; width: 160px;
    display: flex; flex-direction: column; align-items: center; gap: 14px;
  }
  .charity-logo__dot { width: 62px; height: 62px; border-radius: 50%; background: var(--orange); }
  .charity-logo__name { font-weight: 800; font-size: 24px; color: var(--ink); letter-spacing: 0.5px; }

  .heading { position: absolute; left: 380px; width: 570px; top: 38px; text-align: center; }
  .heading__title {
    font-family: "Raleway", "Montserrat", sans-serif; font-weight: 300;
    font-size: 54px; line-height: 1; color: var(--maroon); letter-spacing: 0.5px;
  }
  .heading__intro { margin-top: 12px; font-size: 14.5px; line-height: 1.35; font-weight: 400; }

  .price-badge { position: absolute; left: 1046px; top: 22px; width: 124px; height: 124px; }

  .prize-art { position: absolute; inset: 0; }
  .prize-art__chest {
    position: absolute; left: 118px; top: 410px; width: 380px; height: 368px;
    border-radius: 48% 48% 22% 22% / 30% 30% 14% 14%;
    background: radial-gradient(ellipse at 50% 38%, #f4cf6a 0%, #d8a34a 38%, #b1743a 70%, rgba(150,90,45,0.85) 100%);
  }
  .prize-coin {
    position: absolute; border-radius: 50%;
    display: flex; align-items: center; justify-content: center;
    background: radial-gradient(circle at 40% 35%, #fbe7a0 0%, var(--gold-mid) 60%, var(--gold-dark) 100%);
    border: 6px solid #f3cf6a;
    box-shadow: inset 0 0 0 5px rgba(169,122,37,0.55);
    color: var(--white); font-weight: 800; letter-spacing: -1px;
    text-shadow: 0 2px 0 rgba(120,80,20,0.55);
  }
  .prize-coin--100 { left: 165px; top: 149px; width: 228px; height: 228px; font-size: 62px; }
  .prize-coin--50  { left: 118px; top: 334px; width: 146px; height: 146px; font-size: 44px; }
  .prize-coin--10  { left: 306px; top: 320px; width: 120px; height: 120px; font-size: 34px; }
  .prize-coin--1   { left: 240px; top: 426px; width: 96px;  height: 96px;  font-size: 24px; }

  .photo-frame {
    position: absolute; left: 526px; top: 165px; width: 607px; height: 358px;
    background: var(--white); border: 11px solid var(--orange-deep); border-radius: 30px;
    padding: 10px;
  }
  .photo-frame__image {
    width: 100%; height: 100%; border-radius: 18px;
    background: radial-gradient(ellipse at 50% 45%, #d0524c 0%, #b33c40 55%, #8e3a3c 100%);
  }

  .match-line {
    position: absolute; left: 521px; width: 617px; top: 544px;
    text-align: center; font-weight: 700; font-size: 17px; letter-spacing: 0.3px;
  }

  .scratch-panel {
    position: absolute; left: 521px; top: 581px; width: 617px; height: 198px;
    background: linear-gradient(90deg, #e2b24a 0%, #f5d98a 18%, #cfa14a 45%, #b98a3c 62%, #f0cf7a 82%, #c9963e 100%);
  }

  .how-to-win { position: absolute; left: 521px; top: 795px; width: 617px; }
  .how-to-win__title { font-weight: 700; font-size: 17px; letter-spacing: 0.3px; }
  .how-to-win__text { margin-top: 4px; font-size: 15px; line-height: 1.35; text-align: justify; }

  .age-mark {
    position: absolute; left: 38px; top: 798px; width: 56px; height: 56px;
    border: 3px solid var(--white); border-radius: 50%;
    display: flex; align-items: center; justify-content: center;
    color: var(--white); font-weight: 700; font-size: 18px;
  }
  .operator {
    position: absolute; left: 122px; top: 804px; width: 100px;
    color: var(--white); font-weight: 700; font-size: 14px; line-height: 1.15;
  }
  .responsible {
    position: absolute; left: 228px; top: 806px; width: 232px;
    text-align: center; color: var(--white); font-size: 15px; line-height: 1.3;
  }
  .responsible__url { font-weight: 700; }
</style>
</head>
<body>
<main class="card">

  <svg class="frame" viewBox="0 0 1200 889" aria-hidden="true">
    <path d="M0,0 H272 Q244,6 244,44 V120 Q244,160 204,160 H40 Q0,160 0,205 Z" fill="#ee4b23"/>
    <path d="M0,0 H256 Q230,6 230,44 V114 Q230,146 198,146 H32 Q0,146 0,178 Z" fill="#ffffff"/>
  </svg>

  <div class="charity-logo">
    <span class="charity-logo__dot"></span>
    <span class="charity-logo__name">LIFTWELL</span>
  </div>

  <header class="heading">
    <h1 class="heading__title">The Charity’s Name</h1>
    <p class="heading__intro">Lorem ipsum dolor sit amet, consectetur adipisicing elit,<br>sed do eiusmod tempor incididunt ut labore et dolore magna aliqua.</p>
  </header>

  <svg class="price-badge" viewBox="0 0 124 124" aria-label="Just £1 to play">
    <defs>
      <path id="badge-ring" d="M62,62 m-48,0 a48,48 0 1,1 96,0 a48,48 0 1,1 -96,0"/>
    </defs>
    <circle cx="62" cy="62" r="61" fill="#ee4b23"/>
    <circle cx="62" cy="62" r="56" fill="#6a1b24"/>
    <circle cx="62" cy="62" r="37" fill="#ee4b23"/>
    <text font-family="Montserrat, sans-serif" font-weight="700" font-size="10.5" fill="#ffffff" letter-spacing="0.4">
      <textPath href="#badge-ring">Just £1 to Play - Just £1 to Play - Just £1 to Play -</textPath>
    </text>
    <text x="62" y="77" text-anchor="middle" font-family="Montserrat, sans-serif" font-weight="800" font-size="40" fill="#ffffff">£1</text>
  </svg>

  <div class="prize-art">
    <div class="prize-art__chest" role="img" aria-label="Illustration area: open treasure chest full of gold coins with stars"></div>
    <div class="prize-coin prize-coin--100">£100</div>
    <div class="prize-coin prize-coin--50">£50</div>
    <div class="prize-coin prize-coin--10">£10</div>
    <div class="prize-coin prize-coin--1">£1</div>
  </div>

  <figure class="photo-frame">
    <div class="photo-frame__image" role="img" aria-label="Replaceable client photograph, such as the supported club's team"></div>
  </figure>

  <p class="match-line">MATCH 3 TO WIN THE AMOUNT SHOWN!</p>

  <div class="scratch-panel" aria-label="Scratch-off panel"></div>

  <section class="how-to-win">
    <h2 class="how-to-win__title">HOW TO WIN</h2>
    <p class="how-to-win__text">Lorem ipsum dolor sit amet, consectetur adipisicing elit, sed do eiusmod tempor incididunt ut labore et dolore magna aliqua.</p>
  </section>

  <div class="age-mark">+16</div>
  <div class="operator">Kestrel Prize Services</div>
  <p class="responsible">Please play responsibly<br><span class="responsible__url">www.KeelbrookTrust.org.</span></p>

</main>
</body>
</html>
```